Bright Arch Group business card

Bright Arch Group is the parent company of Bright Arch Building, Bright Arch Plumbing and Bright Arch Renovating. We require a sophisticated business card that covers all aspects of the building and plumbing space without using told or construction items.

Industry/Entity Type

Construction Company

Contact Information for Business Card

Gareth Pimley
Director
0472915083
gareth@brightarch.com.au
Www.brightarch.com.au

Font styles to use
Serif
Sans Serif

Colors
3176b5
ffce3e
0692cd
34a7d8
fbee3e
faa54b

Requirements
Must have
• Logo on front
• Logo and details on rear.
Nice to have
• Maybe water mark or shadow effect with logo
Should not have
• Tools or any construction associated items

```html
<!DOCTYPE html>
<html lang="en">
<head>
<meta charset="utf-8">
<title>Bright Arch Group — Business Card</title>
<link href="https://fonts.googleapis.com/css2?family=Jost:wght@300&family=Didact+Gothic&family=Mulish:wght@700&display=swap" rel="stylesheet">
<style>
  :root {
    --brand-blue: #3176b5;
    --brand-yellow: #ffce3e;
    --card-white: #ffffff;
    --ink-dark: #2a2a2a;
    --divider: #9a9a9a;
    --backdrop: #e9e9e9;
  }
  * { margin: 0; padding: 0; box-sizing: border-box; }
  html, body { width: 1200px; height: 1000px; overflow: hidden; }
  body { background: var(--backdrop); position: relative; }

  .card {
    position: absolute;
    left: 287px;
    width: 627px;
    height: 358px;
    box-shadow: 0 2px 6px rgba(0,0,0,0.18);
  }
  .card--front { top: 140px; background: var(--brand-blue); }
  .card--back  { top: 532px; background: var(--card-white); }

  .wordmark {
    font-family: "Jost", sans-serif;
    font-weight: 300;
    text-align: center;
    line-height: 1;
    text-transform: uppercase;
  }
  .wordmark__mark {
    display: block;
    margin: 0 auto;
    border-radius: 50%;
    background: var(--brand-yellow);
  }

  .card--front .wordmark {
    position: absolute;
    left: 0; right: 0;
    top: 102px;
    color: var(--card-white);
  }
  .card--front .wordmark__mark { width: 40px; height: 40px; margin-bottom: 30px; }
  .card--front .wordmark__name { font-size: 56px; letter-spacing: 9px; }
  .card--front .wordmark__sub { font-size: 32px; letter-spacing: 14px; margin-top: 10px; }

  .front__web {
    position: absolute;
    left: 0; right: 0;
    top: 311px;
    text-align: center;
    font-family: "Didact Gothic", sans-serif;
    font-size: 15px;
    color: var(--card-white);
    letter-spacing: 0.3px;
  }

  .card--back .wordmark {
    position: absolute;
    left: 30px;
    width: 270px;
    top: 128px;
    color: var(--brand-blue);
  }
  .card--back .wordmark__mark { width: 24px; height: 24px; margin-bottom: 14px; }
  .card--back .wordmark__name { font-size: 27px; letter-spacing: 4px; }
  .card--back .wordmark__sub { font-size: 17px; letter-spacing: 7px; margin-top: 5px; }

  .back__divider {
    position: absolute;
    left: 313px;
    top: 128px;
    width: 1px;
    height: 100px;
    background: var(--divider);
  }
  .contact {
    position: absolute;
    left: 337px;
    top: 124px;
    font-family: "Didact Gothic", sans-serif;
    color: var(--ink-dark);
  }
  .contact__name {
    font-family: "Mulish", sans-serif;
    font-weight: 700;
    font-size: 16px;
    color: var(--brand-blue);
  }
  .contact__role { font-size: 14px; margin-top: 2px; }
  .contact__list { list-style: none; margin-top: 13px; }
  .contact__item {
    display: flex;
    align-items: center;
    gap: 7px;
    font-size: 15px;
    line-height: 20px;
  }
  .contact__icon { width: 11px; height: 11px; flex: none; }
</style>
</head>
<body>

<section class="card card--front">
  <div class="wordmark">
    <span class="wordmark__mark"></span>
    <div class="wordmark__name">Bright Arch</div>
    <div class="wordmark__sub">Group</div>
  </div>
  <p class="front__web">www.brightarch.com.au</p>
</section>

<section class="card card--back">
  <div class="wordmark">
    <span class="wordmark__mark"></span>
    <div class="wordmark__name">Bright Arch</div>
    <div class="wordmark__sub">Group</div>
  </div>

  <div class="back__divider"></div>

  <div class="contact">
    <p class="contact__name">Gareth Pimley</p>
    <p class="contact__role">Director</p>
    <ul class="contact__list">
      <li class="contact__item">
        <svg class="contact__icon" viewBox="0 0 12 12" aria-hidden="true">
          <rect x="3" y="0.5" width="6" height="11" rx="1.2" fill="none" stroke="#ffce3e" stroke-width="1.2"/>
          <rect x="5" y="9" width="2" height="1" fill="#ffce3e"/>
        </svg>
        0472915083
      </li>
      <li class="contact__item">
        <svg class="contact__icon" viewBox="0 0 12 12" aria-hidden="true">
          <rect x="0.5" y="2.5" width="11" height="7.5" fill="#ffce3e"/>
          <path d="M0.5 2.5 L6 7 L11.5 2.5" fill="none" stroke="#ffffff" stroke-width="1"/>
        </svg>
        gareth@brightarch.com.au
      </li>
      <li class="contact__item">
        <svg class="contact__icon" viewBox="0 0 12 12" aria-hidden="true">
          <circle cx="6" cy="6" r="5" fill="none" stroke="#ffce3e" stroke-width="1.1"/>
          <ellipse cx="6" cy="6" rx="2.2" ry="5" fill="none" stroke="#ffce3e" stroke-width="1"/>
          <line x1="1" y1="6" x2="11" y2="6" stroke="#ffce3e" stroke-width="1"/>
        </svg>
        www.brightarch.com.au
      </li>
    </ul>
  </div>
</section>

</body>
</html>
```